Business cards Dör Kornhüüs GmbH & Co.KG

We need a uniform business card design template for our employees.
A template should be created to have the same design for all business cards.

Contact Information for Business Card

Firma und Firmierung, Name, Funktion in Unternehmen, Anschrift, Tel. Handynummer, Emailadresse, Internetseite

Colors

Designer to choose colors to be used in the design.

Requirements
Must have
• Our company logo must be on it

```html
<!DOCTYPE html>
<html lang="de">
<head>
<meta charset="utf-8">
<title>Dör Kornhüüs – Visitenkarte</title>
<link href="https://fonts.googleapis.com/css2?family=Lato:wght@400;700&family=Montserrat:wght@700&display=swap" rel="stylesheet">
<style>
  :root {
    --backdrop: #2b2b2d;
    --card: #1c1d1f;
    --card-pattern: #242527;
    --rose: #ea7795;
    --lilac: #c49ad8;
    --ink: #f4f2f2;
    --rule: #6c6c70;
  }
  * { box-sizing: border-box; margin: 0; padding: 0; }
  html, body { width: 1200px; height: 1108px; overflow: hidden; background: var(--backdrop); }
  .canvas { position: relative; width: 1200px; height: 1108px; }

  .card {
    position: absolute; top: 234px; width: 410px; height: 640px;
    background: var(--card); border-radius: 24px; overflow: hidden;
  }
  .card--front { left: 150px; }
  .card--back { left: 640px; }

  .brand { position: absolute; top: 118px; left: 0; right: 0; text-align: center; }
  .brand__name {
    font-family: 'Lato', sans-serif; font-weight: 700; font-size: 40px;
    color: var(--rose); letter-spacing: 1px;
  }
  .brand__tagline {
    margin-top: 6px; font-family: 'Lato', sans-serif; font-size: 15px;
    color: var(--lilac); letter-spacing: 3px;
  }

  .person { position: absolute; top: 352px; left: 0; right: 0; text-align: center; }
  .person__name {
    font-family: 'Montserrat', sans-serif; font-weight: 700; font-size: 22px;
    color: var(--rose); letter-spacing: 0.5px;
  }
  .person__role { font-family: 'Lato', sans-serif; font-size: 18px; color: var(--ink); margin-top: 2px; }

  .icon-row { position: absolute; top: 420px; left: 40px; right: 40px; height: 26px; }
  .icon-row svg { display: block; }

  .contact {
    position: absolute; top: 462px; left: 0; right: 0; text-align: center;
    font-family: 'Lato', sans-serif; font-size: 18px; line-height: 27px; color: var(--ink);
  }
  .contact__rule { width: 200px; height: 1px; background: var(--rule); margin: 10px auto 10px; }

  .back-pattern { position: absolute; inset: 0; background: linear-gradient(160deg, var(--card-pattern), var(--card) 75%); }
  .back-mark {
    position: absolute; bottom: 170px; left: 0; right: 0; text-align: center;
    font-family: 'Lato', sans-serif; font-weight: 700; font-size: 22px; color: var(--rose);
  }
</style>
</head>
<body>
<div class="canvas">

  <section class="card card--front" aria-label="Vorderseite">
    <div class="brand">
      <div class="brand__name">Dör Kornhüüs</div>
      <div class="brand__tagline">Nordische Backkunst</div>
    </div>

    <div class="person">
      <div class="person__name">LUKAS BERGER</div>
      <div class="person__role">Managing Director</div>
    </div>

    <div class="icon-row">
      <svg width="330" height="26" viewBox="0 0 330 26">
        <line x1="0" y1="13" x2="120" y2="13" stroke="#6c6c70" stroke-width="1.5"/>
        <line x1="210" y1="13" x2="330" y2="13" stroke="#6c6c70" stroke-width="1.5"/>
        <g fill="#ea7795">
          <circle cx="136" cy="13" r="12"/>
          <circle cx="165" cy="13" r="12"/>
          <circle cx="194" cy="13" r="12"/>
        </g>
        <g fill="none" stroke="#1c1d1f" stroke-width="1.6" stroke-linecap="round" stroke-linejoin="round">
          <path d="M131 8 q-1 6 5 10 l2-2 -2-2 -1 1 q-2-1-3-4 l1-1 -2-2z"/>
          <rect x="158" y="8" width="14" height="10" rx="1"/>
          <path d="M158 9 l7 5 7-5"/>
          <circle cx="194" cy="13" r="6"/>
          <path d="M188 13 h12 M194 7 q-3 6 0 12 q3-6 0-12"/>
        </g>
      </svg>
    </div>

    <div class="contact">
      <div>040-987 654 321</div>
      <div>hallo@kornhuues-beispiel.de</div>
      <div>www.kornhuues-beispiel.de</div>
      <div class="contact__rule"></div>
      <div>421, Address line here,</div>
      <div>45452, Country Name</div>
    </div>
  </section>

  <section class="card card--back" aria-label="Rückseite">
    <div class="back-pattern" role="img" aria-label="Dezentes, wiederholtes Markenmuster in Dunkelgrau"></div>
    <div class="back-mark">Dör Kornhüüs</div>
  </section>

</div>
</body>
</html>
```